Townhome Multi-Family Property Exterior Sign

Hello. We are looking for a new design for our exterior pylon for for a multi-family housing property in Texas. The design will need to go on a new sign panel to replace the existing (see photo of existing). We are looking to see both modern and contemporary designs. Included the sign should be the name, Loma Brisa Townhomes and the web address www.lomabrisatownhomes.example.

Attached here is a PDF file of the proposed new sign shape. We are open to other shape ideas as well if your design would better suit a more rectangular shape.

Industry/Entity Type

Property

Font styles to use
Serif
Sans Serif

Colors
9bcb3c

Requirements
Must have
• Name of building: Loma Brisa Townhomes
• Website: www.lomabrisatownhomes.example
Nice to have
• Address: 412-590 Halvern Ridge Drive (only if it fits nicely)

```html
<!DOCTYPE html>
<html lang="en">
<head>
<meta charset="utf-8">
<title>Loma Brisa Townhomes – Exterior Sign</title>
<link rel="stylesheet" href="https://fonts.googleapis.com/css2?family=Limelight&family=Raleway:wght@400;700&display=swap">
<style>
  :root {
    --backdrop: #9e9d9e;
    --backdrop-glow: #ececec;
    --sign-green: #9bcb3c;
    --ornament-tone: #84b12f;
    --ink: #231f20;
  }
  html, body {
    margin: 0;
    padding: 0;
    width: 1200px;
    height: 644px;
    overflow: hidden;
    background: var(--backdrop);
  }
  .sign-canvas {
    display: block;
    width: 1200px;
    height: 644px;
  }
  .sign-name {
    font-family: "Limelight", serif;
    font-size: 196px;
    fill: var(--ink);
  }
  .sign-subtitle {
    font-family: "Raleway", sans-serif;
    font-weight: 700;
    font-size: 60px;
    fill: var(--ink);
    letter-spacing: 2px;
  }
  .sign-website {
    font-family: "Raleway", sans-serif;
    font-weight: 400;
    font-size: 26px;
    fill: var(--ink);
  }
</style>
</head>
<body>
<svg class="sign-canvas" viewBox="0 0 1200 644" xmlns="http://www.w3.org/2000/svg">
  <defs>
    <radialGradient id="backdrop-glow" cx="600" cy="90" r="320" gradientUnits="userSpaceOnUse">
      <stop offset="0" stop-color="var(--backdrop-glow)"/>
      <stop offset="1" stop-color="var(--backdrop)"/>
    </radialGradient>
  </defs>

  <rect class="backdrop" width="1200" height="644" fill="url(#backdrop-glow)"/>

  <g class="sign-posts" fill="var(--ink)">
    <rect x="62" y="230" width="48" height="414"/>
    <polygon points="53,228 86,214 120,228 120,236 53,236"/>
    <rect x="1090" y="226" width="46" height="418"/>
    <polygon points="1078,222 1112,209 1146,222 1146,230 1078,230"/>
  </g>

  <path class="sign-panel" fill="var(--sign-green)"
        d="M110,236 C300,232 420,116 600,116 C780,116 900,232 1090,238 L1090,604 L110,604 Z"/>

  <path class="sign-frame" fill="var(--ink)" fill-rule="evenodd"
        d="M122,260 C310,254 430,138 600,138 C770,138 890,254 1078,262 L1078,582 L122,582 Z
           M136,274 C320,268 440,153 600,153 C760,153 880,268 1064,276 L1064,568 L136,568 Z"/>

  <path class="sign-inner-rule" fill="none" stroke="var(--ink)" stroke-width="2"
        d="M140,286 C325,280 445,164 600,164 C755,164 875,280 1060,288 L1060,562 L140,562 Z"/>

  <rect class="sign-ornament" role="img" aria-label="Decorative scroll flourish crowning the sign"
        x="446" y="162" width="306" height="100" rx="40" fill="var(--ornament-tone)"/>

  <text class="sign-name" x="600" y="432" text-anchor="middle" textLength="800" lengthAdjust="spacingAndGlyphs">Loma Brisa</text>

  <rect class="sign-subtitle-rule" x="200" y="478" width="256" height="8" fill="var(--ink)"/>
  <text class="sign-subtitle" x="462" y="496" textLength="510" lengthAdjust="spacingAndGlyphs">TOWNHOMES</text>

  <text class="sign-website" x="600" y="546" text-anchor="middle">www.lomabrisatownhomes.example</text>
</svg>
</body>
</html>
```